KelvaNest - Home Income and Business Resources Platform

I am looking for a website template for a multi-purposed website. This website will feature:

1.) Website Directory with Ratings & comments on listings
2.) Company Blog
3.) Homepage with Content (see files for homepage mock)

I would like the Design to have a default width 1170px (wider then normal)

Of course I am looking for Pages for Listings to be designed.

Great looking BLOG Layout: http://journal.pixelvorn.example/html/blog.html

I would like 4 Versions of a Website Directory Listing "Box"
1.) Basic Listing Box
2.) Sponsored Listing Box
3.) Recommended Listing Box
4.) Stay Away From Listing Box

Information on the Listing Page (Like on a Category Page)
Site Name, Site URL, Website Image, # of Views, Rating and # of Comments

Information on the Listing Details Page:
Same as ABOVE + About website Description, Trovix Rank, Category Information

Decent looking examples is here: https://demos.quendaro.example/directory/computers/ and http://www.zibrankhub.example/.

I will include some sketches and screenshots of things I like/looking for. As designers,you have creative freedom and are encouraged to show this. This is Phase one of this project and winning designer is guaranteed to have future work for this project.

Target Market(s)

Directory, business, websites

Industry/Entity Type

Business

Font styles to use
Sans Serif

Colors

Designer to choose colors to be used in the design.

Requirements
Must have
• Professional yet clean look. The use of Icons & images
• Unique Look
Should not have
• Any exact copies of any examples I provided

```html
<!DOCTYPE html>
<html lang="en">
<head>
<meta charset="utf-8">
<title>KelvaNest – Home Income and Business Resources</title>
<link rel="stylesheet" href="https://fonts.googleapis.com/css2?family=Roboto:wght@400;700;900&family=Roboto+Condensed:wght@400;700&family=Open+Sans:wght@400&display=swap">
<style>
:root{
  --bg-top:#5bb8dc;
  --bg-mid:#3f9ad0;
  --bg-bottom:#2f74b8;
  --white:#ffffff;
  --green:#6cb614;
  --orange:#e59f3b;
  --sky:#6ec3db;
  --sponsor-head:#4fc1e2;
  --sponsor-body:#f7f7f7;
  --sponsor-logo:#9a9a9a;
  --slide-dark:#3a4a5c;
}
*{margin:0;padding:0;box-sizing:border-box}
html,body{width:1200px;height:1007px;overflow:hidden}
body{
  position:relative;
  font-family:"Roboto",sans-serif;
  color:var(--white);
  background:
    linear-gradient(135deg,rgba(255,255,255,.18) 0%,rgba(255,255,255,0) 40%),
    linear-gradient(160deg,var(--bg-top) 0%,var(--bg-mid) 50%,var(--bg-bottom) 100%);
}
.site-logo{position:absolute;left:99px;top:32px;font-size:40px;font-weight:900;letter-spacing:.5px}
.main-nav{position:absolute;top:48px;left:667px;display:flex;gap:0;font-family:"Roboto Condensed",sans-serif;font-size:15.5px}
.main-nav a{color:var(--white);text-decoration:none;position:absolute;white-space:nowrap}
.content-panel{position:absolute;left:81px;top:113px;width:1037px;height:716px;background:var(--white);border-radius:29px;box-shadow:0 4px 14px rgba(0,0,0,.15)}
.hero-slide{position:absolute;left:99px;top:130px;width:763px;height:359px;background:linear-gradient(90deg,#8e9aa6 0%,#5d6b7a 45%,var(--slide-dark) 100%)}
.hero-title{position:absolute;left:431px;top:196px;font-family:"Roboto Condensed",sans-serif;font-weight:700;font-size:41px;white-space:nowrap}
.hero-text{position:absolute;left:431px;top:246px;font-size:14px;line-height:22px}
.hero-dots{position:absolute;left:431px;top:307px;display:flex;gap:8px}
.hero-dots span{width:14px;height:14px;border-radius:50%;border:1.5px solid var(--white)}
.hero-dots span.active{background:var(--white)}
.feature-card{position:absolute;top:506px;width:241px;height:304px;text-align:center}
.feature-card.green{left:99px;background:var(--green)}
.feature-card.orange{left:360px;background:var(--orange)}
.feature-card.sky{left:621px;background:var(--sky)}
.feature-icon{width:86px;height:86px;border-radius:50%;background:var(--white);margin:23px auto 0;display:flex;align-items:center;justify-content:center}
.feature-title{margin-top:14px;font-size:17.5px;line-height:21px;font-weight:400}
.feature-text{margin:13px 16px 0;font-family:"Open Sans",sans-serif;font-size:11.3px;line-height:20.5px}
.read-more{display:inline-block;margin-top:10px;font-family:"Roboto Condensed",sans-serif;font-size:12.5px;color:var(--white);text-decoration:none}
.read-more svg{margin-left:8px;vertical-align:middle}
.sponsor-box{position:absolute;left:887px;top:130px;width:214px;height:284px;background:var(--sponsor-body);border:1px solid #e6e6e6}
.sponsor-head{height:39px;background:var(--sponsor-head);display:flex;align-items:center;justify-content:space-between;padding:0 16px;font-family:"Roboto Condensed",sans-serif;font-size:19px}
.sponsor-list{list-style:none;text-align:center;color:var(--sponsor-logo);padding-top:24px}
.sponsor-list li{height:52px;display:flex;align-items:center;justify-content:center;gap:6px;font-size:24px}
.sponsor-list .dot{width:14px;height:14px;border-radius:50%;background:var(--sponsor-logo)}
.sponsor-list .tile{background:#a7a7a7;color:var(--white);padding:2px 10px}
.ad-banner{position:absolute;left:887px;width:214px}
.ad-one{top:440px;height:163px;background:linear-gradient(180deg,#f3e7cc,#e9d8b0);border:1px solid #e5b7a3}
.ad-two{top:628px;height:182px;background:linear-gradient(160deg,#ff6a2e,#f2561f);border:1px solid #e5b7a3}
.social-links{position:absolute;top:879px;left:513px;display:flex;gap:13px}
.social-links span{width:24px;height:24px;border-radius:4px;background:var(--white)}
.footer-nav{position:absolute;top:921px;left:0;width:1200px;text-align:center;font-family:"Open Sans",sans-serif;font-size:13.5px}
.footer-nav a{color:var(--white);text-decoration:none}
.footer-nav .sep{margin:0 8px}
.copyright{position:absolute;top:952px;left:0;width:1200px;text-align:center;font-family:"Open Sans",sans-serif;font-size:12.8px}
</style>
</head>
<body>
<div class="site-logo">KelvaNest</div>
<nav class="main-nav">
  <a href="#" style="left:0">HOME</a>
  <a href="#" style="left:66px">ABOUT US</a>
  <a href="#" style="left:160px">OUR SERVICES</a>
  <a href="#" style="left:288px">BLOG</a>
  <a href="#" style="left:350px">CONTACT US</a>
</nav>

<div class="content-panel"></div>

<section class="hero-slide" role="img" aria-label="Photo of two businessmen discussing work at a laptop in an office">
  <h1 class="hero-title">ABOUT KELVANEST</h1>
  <p class="hero-text">Lorem ipsum dolor sit amet, consectetur adipiscing<br>Sed ut perspiciatis unde sed do eiusmod</p>
  <div class="hero-dots"><span class="active"></span><span></span><span></span></div>
</section>

<article class="feature-card green">
  <div class="feature-icon">
    <svg width="34" height="30" viewBox="0 0 34 30"><path d="M17 2 2 15h4v13h8v-8h6v8h8V15h4z" fill="#6cb614"/><rect x="24" y="3" width="4" height="7" fill="#6cb614"/></svg>
  </div>
  <h2 class="feature-title">Home Income<br>Resource Directory</h2>
  <p class="feature-text">Find what you need, when you need it.The KelvaNest website directory is your one-stop pit for anything involved in making money from</p>
  <a class="read-more" href="#">READ MORE<svg width="8" height="8" viewBox="0 0 8 8"><path d="M1 1l6 6M7 3v4H3" stroke="#fff" fill="none"/></svg></a>
</article>

<article class="feature-card orange">
  <div class="feature-icon">
    <svg width="38" height="34" viewBox="0 0 38 34"><path d="M4 11h8l16-9v28L12 21H4z" fill="#e59f3b"/><path d="M10 21l4 11h5l-3-11z" fill="#e59f3b"/><path d="M31 11q4 5 0 10" stroke="#e59f3b" stroke-width="3" fill="none"/></svg>
  </div>
  <h2 class="feature-title">Advertising<br>Benefits</h2>
  <p class="feature-text">Everyone needs to advertise and we know just how to get your offer out to the right people. We have many methods including: Text ads,</p>
  <a class="read-more" href="#">READ MORE<svg width="8" height="8" viewBox="0 0 8 8"><path d="M1 1l6 6M7 3v4H3" stroke="#fff" fill="none"/></svg></a>
</article>

<article class="feature-card sky">
  <div class="feature-icon">
    <svg width="40" height="32" viewBox="0 0 40 32"><path d="M2 2v28h36" stroke="#6ec3db" stroke-width="3" fill="none"/><path d="M7 24l9-9 6 5 11-11" stroke="#6ec3db" stroke-width="3" fill="none"/><path d="M27 7h7v7" stroke="#6ec3db" stroke-width="3" fill="none"/></svg>
  </div>
  <h2 class="feature-title">Earning With<br>KelvaNest</h2>
  <p class="feature-text">Join KelvaNest and start earning money. When you share KelvaNest and lock in an advertiser or premium listing, we reward you. Build a downline</p>
  <a class="read-more" href="#">READ MORE<svg width="8" height="8" viewBox="0 0 8 8"><path d="M1 1l6 6M7 3v4H3" stroke="#fff" fill="none"/></svg></a>
</article>

<aside class="sponsor-box">
  <div class="sponsor-head">
    <svg width="8" height="12" viewBox="0 0 8 12"><path d="M7 1 2 6l5 5" stroke="#fff" stroke-width="1.6" fill="none"/></svg>
    <span>SPONSORED</span>
    <svg width="8" height="12" viewBox="0 0 8 12"><path d="M1 1l5 5-5 5" stroke="#fff" stroke-width="1.6" fill="none"/></svg>
  </div>
  <ul class="sponsor-list">
    <li><span class="dot"></span>Lumarco</li>
    <li>VANTORAL</li>
    <li>Quessa</li>
    <li><span class="tile">Verdo</span></li>
  </ul>
</aside>

<div class="ad-banner ad-one" role="img" aria-label="Advertising banner with a cartoon illustration about surviving server trouble"></div>
<div class="ad-banner ad-two" role="img" aria-label="Advertising banner with an orange illustrated scene for server management software"></div>

<div class="social-links" aria-label="Social links"><span></span><span></span><span></span><span></span><span></span></div>
<nav class="footer-nav">
  <a href="#">Home</a><span class="sep">/</span><a href="#">Contact</a><span class="sep">/</span><a href="#">services</a><span class="sep">/</span><a href="#">About Us</a><span class="sep">/</span><a href="#">Discussion</a><span class="sep">/</span><a href="#">Videos Links</a>
</nav>
<p class="copyright">Copyright @ 2017 KelvaNest. All Rights Reserved.</p>
</body>
</html>
```